Young and modern Electrical company working in the commercial arena.

Wanting a business card design thats modern and will last. Maybe Minimalist? Happy to look at changing my logo

Target Market(s)

Builders, Project Managers

Industry/Entity Type

Electrical

Contact Information for Business Card

Name
Address
Phone number
Job title

Logo Text

our name or just the logo i'm open to ideas

Font styles to use
Sans Serif

Requirements
Nice to have
• would like to keep the purple in our current logo. it's kinda unique to our market
Should not have
• Don't want it to be to busy. simple is best i think

```html
<!DOCTYPE html>
<html lang="en">
<head>
<meta charset="utf-8">
<title>Hartwell Electrical – Business Card</title>
<link rel="stylesheet" href="https://fonts.googleapis.com/css2?family=Arimo:wght@400;700&display=swap">
<style>
  :root {
    --stage-light: #f4f4f4;
    --stage-mid: #a9a9a9;
    --stage-dark: #777777;
    --card-brown: #976939;
    --card-white: #ffffff;
    --brand-purple: #3a2cf0;
    --accent-red: #ff0000;
    --ink-black: #1c1c1c;
    --arc-grey: #6b6b6b;
    --text-white: #ffffff;
  }
  * { margin: 0; padding: 0; box-sizing: border-box; }
  html, body { width: 1200px; height: 1000px; overflow: hidden; }
  body {
    position: relative;
    font-family: "Arimo", Arial, sans-serif;
    background: radial-gradient(circle at 600px 490px, var(--stage-light) 0, var(--stage-mid) 330px, var(--stage-dark) 620px);
  }
  .card {
    position: absolute;
    left: 288px;
    width: 614px;
    height: 351px;
    overflow: hidden;
  }
  .card--front { top: 104px; background: var(--card-brown); }
  .card--back { top: 503px; background: var(--card-white); }

  .brand-name {
    font-weight: 400;
    color: var(--brand-purple);
    white-space: nowrap;
    letter-spacing: 0.5px;
  }
  .card--front .brand-name {
    position: absolute;
    left: 0; right: 0;
    top: 160px;
    text-align: center;
    font-size: 36px;
  }

  .back-art { position: absolute; inset: 0; }
  .back-art .arc-grey { fill: var(--arc-grey); }
  .back-art .arc-black { fill: var(--ink-black); }
  .back-art .panel-brown { fill: var(--card-brown); }
  .back-art .crescent-red { fill: var(--accent-red); }

  .card--back .brand-name {
    position: absolute;
    left: 532px;
    top: 177px;
    font-size: 27px;
    transform: translate(-50%, -50%) rotate(-90deg);
  }

  .name-plate {
    position: absolute;
    left: 22px; top: 33px;
    width: 291px; height: 65px;
    border-radius: 12px;
    background: linear-gradient(90deg, var(--accent-red) 0%, var(--accent-red) 22%, #b8383a 30%, #3a2626 45%, var(--ink-black) 70%, #2a2a2a 100%);
    color: var(--text-white);
    text-align: center;
    font-weight: 700;
  }
  .name-plate .person-name { display: block; font-size: 26px; line-height: 1; padding-top: 15px; padding-left: 10px; }
  .name-plate .job-title { display: block; font-size: 13px; line-height: 1; margin-top: -3px; margin-right: 44px; }

  .contact-list { position: absolute; left: 32px; top: 135px; list-style: none; }
  .contact-item {
    display: flex; align-items: center;
    height: 36px; margin-bottom: 30px;
    color: var(--accent-red);
    font-size: 18px;
  }
  .contact-item:nth-child(2) { margin-bottom: 31px; }
  .contact-icon { width: 36px; height: 36px; margin-right: 13px; flex: none; }
  .contact-icon circle { fill: var(--accent-red); }
  .contact-icon .glyph { fill: var(--card-white); }
  .contact-icon .glyph-line { fill: none; stroke: var(--accent-red); stroke-width: 1.3; }
  .contact-item--address span { padding-left: 6px; }
</style>
</head>
<body>
  <section class="card card--front" aria-label="Card front">
    <p class="brand-name">hartwell electrical</p>
  </section>

  <section class="card card--back" aria-label="Card back">
    <svg class="back-art" viewBox="0 0 614 351" width="614" height="351" aria-hidden="true">
      <path class="arc-grey" d="M395,0 C365,40 357,110 362,185 L614,185 L614,0 Z"/>
      <path class="arc-black" d="M363,160 C358,240 378,310 418,351 L614,351 L614,160 Z"/>
      <path class="panel-brown" d="M412,0 C387,50 382,120 385,180 C388,250 402,310 432,351 L614,351 L614,0 Z"/>
      <path class="crescent-red" d="M552,0 C430,20 369,110 369,176 C369,255 430,335 552,351 C460,320 397,255 397,176 C397,100 460,30 552,0 Z"/>
    </svg>
    <p class="brand-name">hartwell electrical</p>

    <div class="name-plate">
      <span class="person-name">MY NAME</span>
      <span class="job-title">Job Title</span>
    </div>

    <ul class="contact-list">
      <li class="contact-item contact-item--phone">
        <svg class="contact-icon" viewBox="0 0 36 36" aria-hidden="true">
          <circle cx="18" cy="18" r="18"/>
          <path class="glyph" d="M12.5,10 L15.5,10 L17,14 L15.2,15.6 C16,17.6 18,19.8 20.3,20.8 L21.9,19 L26,20.5 L26,23.5 C26,24.6 25,25.5 23.8,25.4 C17,24.8 11.2,19 10.6,12.2 C10.5,11 11.4,10 12.5,10 Z"/>
        </svg>
        <span>+ 234 7000000000</span>
      </li>
      <li class="contact-item contact-item--email">
        <svg class="contact-icon" viewBox="0 0 36 36" aria-hidden="true">
          <circle cx="18" cy="18" r="18"/>
          <rect class="glyph" x="9" y="12" width="18" height="12" rx="1"/>
          <path class="glyph-line" d="M9.5,12.5 L18,19 L26.5,12.5 M9.5,23.5 L15.5,17.5 M26.5,23.5 L20.5,17.5"/>
        </svg>
        <span>example@mailbox.com</span>
      </li>
      <li class="contact-item contact-item--address">
        <svg class="contact-icon" viewBox="0 0 36 36" aria-hidden="true">
          <circle cx="18" cy="18" r="18"/>
          <path class="glyph" d="M18,8.5 C14.2,8.5 11.5,11.3 11.5,15 C11.5,19.5 18,27.5 18,27.5 C18,27.5 24.5,19.5 24.5,15 C24.5,11.3 21.8,8.5 18,8.5 Z"/>
          <circle cx="18" cy="15" r="2.6"/>
        </svg>
        <span>9, address street.</span>
      </li>
    </ul>
  </section>
</body>
</html>
```